modernized upgrade to existing squarespace site

Hello! I have the following page for my consulting firm: https://fernwaystrategygroup.com/ Would love to upgrade to something more modern/attractive like here: https://www.lobrettiandco.com/ or https://quillbrightlab.com/ , but I am open to creativity. Would like to retain the logo look and color theme from the logo. The rest can be left to creative discretion.

```html
<!DOCTYPE html>
<html lang="en">
<head>
<meta charset="utf-8">
<title>Fernway Strategy Group</title>
<link href="https://fonts.googleapis.com/css2?family=Marcellus&family=Poppins:wght@400;500;600&display=swap" rel="stylesheet">
<style>
:root{
  --ink:#0d0d0d;
  --white:#ffffff;
  --rose:#c4918a;
  --rose-deep:#b07d76;
  --rose-text:#d89b8f;
  --grey-band:#4a4a4a;
  --line:#6b6b6b;
  --serif:'Marcellus', Georgia, serif;
  --sans:'Poppins', Arial, sans-serif;
}
*{box-sizing:border-box;margin:0;padding:0}
html,body{width:1200px;height:3659px;overflow:hidden;background:var(--ink)}
body{font-family:var(--sans);color:var(--white)}
.page{position:relative;width:1200px;height:3659px;overflow:hidden;background:var(--ink)}
.abs{position:absolute}
svg{display:block}

/* header */
.brand{position:absolute;display:flex;align-items:center;gap:10px}
.brand-box{border:1.5px solid var(--white)}
.brand-name{font-family:var(--serif);color:var(--white);line-height:1.05;letter-spacing:.16em}
.site-header .brand{left:121px;top:18px}
.site-header .brand-box{width:38px;height:38px}
.site-header .brand-name{font-size:13px}
.nav{position:absolute;left:434px;top:30px;display:flex;gap:42px;font-size:12px}
.nav a{color:var(--white);text-decoration:none}
.nav a.active{color:var(--rose-text)}
.header-icon{position:absolute;top:27px;width:24px;height:24px;border:1.3px solid var(--white);border-radius:50%}
.btn-outline{position:absolute;display:flex;align-items:center;justify-content:center;border:1.5px solid var(--white);font-size:10.5px;font-weight:500;letter-spacing:.04em;color:var(--white);text-transform:uppercase}

/* hero */
.hero-photo{left:0;top:0;width:1200px;height:587px;background:linear-gradient(180deg,#3b3d44 0%,#7b6250 38%,#a6733f 52%,#4d4136 72%,#1d1b1a 100%)}
.hero-frame{left:873px;top:109px;width:240px;height:478px;border:3px solid var(--white);border-bottom:none}
.hero-title{left:105px;top:250px;font-family:var(--serif);font-size:104px;letter-spacing:.08em;line-height:1}
.hero-sub{left:118px;top:362px;font-family:var(--serif);font-size:37px;line-height:45px;letter-spacing:.01em}
.play{position:absolute;border-radius:50%;background:var(--white);display:flex;align-items:center;justify-content:center}

/* section titles */
.section-title{position:absolute;font-family:var(--serif);font-size:36px;font-weight:400;text-align:center;width:1200px;left:0}

/* services */
.service{position:absolute;top:679px;width:304px;height:361px;background:var(--white)}
.service-icon{position:absolute;left:6px;top:6px;width:66px;height:60px;background:var(--rose);display:flex;align-items:center;justify-content:center}
.service-label{position:absolute;left:6px;top:74px;font-size:17.5px;color:#222;display:flex;align-items:center;gap:10px}
.service-photo{position:absolute;left:6px;top:116px;width:292px;height:239px}

/* about */
.about{left:122px;top:1146px;width:956px;height:588px;background:var(--rose)}
.about-title{left:12px;top:50px;font-family:var(--serif);font-size:38px;display:flex;align-items:center;gap:8px}
.about-title::after{content:"";display:block;width:66px;height:1.5px;background:var(--white);margin-top:10px}
.about-text{left:11px;top:95px;width:470px;font-size:10.8px;line-height:15px}
.about-frame{left:381px;top:175px;width:406px;height:383px;border:1px solid #3a2b29}
.about-photo{left:10px;top:183px;width:765px;height:393px;background:linear-gradient(160deg,#22302f 0%,#182220 45%,#0f1514 100%)}
.about-vertical{right:-14px;top:0;height:588px;writing-mode:vertical-rl;font-family:var(--serif);font-size:100px;line-height:1;letter-spacing:.02em;color:var(--white);text-align:center}

/* partners */
.partner{position:absolute;top:1842px;width:182px;height:111px;background:var(--white);display:flex;align-items:center;justify-content:center;text-align:center;font-family:var(--sans);font-weight:600;font-size:19px;color:#3a3a3a;line-height:1.15;padding:0 12px}
.carousel-dot{position:absolute;top:1886px;width:20px;height:20px;border-radius:50%;background:#bdbdbd;display:flex;align-items:center;justify-content:center}

/* testimonial */
.testimonial-band{left:0;top:2014px;width:1200px;height:477px;background:linear-gradient(90deg,#515151 0%,#3f3f3f 55%,#5a5a5a 100%)}
.testimonial-ghost{left:-6px;top:2352px;font-family:var(--serif);font-size:170px;line-height:1;color:rgba(255,255,255,.07);letter-spacing:.02em;white-space:nowrap}
.testimonial-title{left:120px;top:2068px;font-family:var(--serif);font-size:37px}
.avatar{left:123px;top:2130px;width:50px;height:50px;border-radius:50%;background:linear-gradient(180deg,#8f8a86,#3d3f44)}
.reviewer{left:194px;top:2135px;font-size:14px;font-weight:500}
.reviewer small{font-size:10.5px;font-weight:400;margin-left:6px}
.stars{left:193px;top:2156px;display:flex;gap:3px}
.quote-text{left:122px;top:2226px;width:356px;font-size:10.8px;line-height:18px;color:#e6e6e6}
.arrow-pair{left:124px;top:2315px;display:flex;gap:2px}
.arrow-pair span{width:64px;height:35px;background:var(--rose);display:flex;align-items:center;justify-content:center}
.portrait-frame{left:700px;top:2114px;width:378px;height:377px;border:11px solid var(--white);border-bottom:none}
.portrait{left:711px;top:2038px;width:356px;height:441px;background:linear-gradient(180deg,rgba(90,90,90,0) 0%,#3a3d44 30%,#1f2228 100%)}

/* news */
.news-feature{left:132px;top:2552px;width:489px;height:278px;background:linear-gradient(135deg,#1c3a55 0%,#3e7d9c 45%,#a9d6e8 60%,#35647f 100%)}
.news-strip{left:625px;top:2552px;width:31px;height:278px;background:var(--rose);writing-mode:vertical-rl;transform:rotate(180deg);font-family:var(--serif);font-size:16px;letter-spacing:.06em;display:flex;align-items:center;justify-content:center;color:#3a2522}
.news-date{display:flex;align-items:center;gap:8px;font-family:var(--serif);font-size:10.5px;color:var(--rose-text);text-decoration:underline}
.news-head{font-size:15.5px;line-height:22px}
.news-arrow{color:var(--rose-text)}
.latest-title{left:744px;top:2540px;font-family:var(--serif);font-size:36px}
.thumb{position:absolute;left:744px;width:126px;height:90px}
.news-item{position:absolute;left:885px;width:200px}
.news-item .news-head{font-size:13.5px;line-height:18px;margin-top:6px}

/* contact */
.map{left:0;top:2978px;width:654px;height:441px;background:linear-gradient(135deg,#e7ece6 0%,#dfe8e0 40%,#cfe0ea 70%,#e8ece8 100%)}
.map-card{left:203px;top:3182px;width:216px;height:70px;background:var(--white);color:#222;font-size:12.5px;text-align:center;line-height:18px;display:flex;align-items:center;justify-content:center;box-shadow:0 2px 6px rgba(0,0,0,.15)}
.contact-panel{left:654px;top:2978px;width:546px;height:441px;background:var(--rose)}
.contact-title{left:722px;top:3030px;font-family:var(--serif);font-size:34px;line-height:38px}
.contact-sub{left:723px;top:3106px;font-size:13px}
.field{position:absolute;left:724px;width:352px;border:1px solid rgba(255,255,255,.85);font-size:11.5px;padding:9px 11px}
.submit{left:724px;top:3327px;width:96px;height:36px;background:#111;font-size:11px;font-weight:600;display:flex;align-items:center;justify-content:center}

/* footer */
.site-footer .brand{left:122px;top:3500px}
.site-footer .brand-box{width:56px;height:56px}
.site-footer .brand-name{font-size:27px}
.site-footer .brand-name span{display:block;font-size:14px;margin-top:4px}
.footer-divider{position:absolute;top:3451px;width:1px;height:163px;background:var(--line)}
.footer-heading{position:absolute;top:3452px;font-family:var(--serif);font-size:19px}
.footer-links{position:absolute;left:478px;top:3481px;list-style:none;font-size:9.5px;line-height:20.6px}
.contact-row{position:absolute;left:706px;display:flex;align-items:center;gap:8px;font-size:9.3px;line-height:13px}
.ring{width:18px;height:18px;border:1.2px solid var(--white);border-radius:50%;display:flex;align-items:center;justify-content:center;flex:none}
.social-row{position:absolute;left:998px;display:flex;align-items:center;gap:8px;font-size:9.3px}
.footer-rule{left:122px;top:3625px;width:956px;height:1px;background:var(--line)}
.copyright{left:0;top:3637px;width:1200px;text-align:center;font-size:8.5px}
</style>
</head>
<body>
<div class="page">

  <!-- hero -->
  <div class="abs hero-photo" role="img" aria-label="City skyline at dusk with an observation tower and mountains behind"></div>
  <div class="abs hero-frame"></div>

  <header class="site-header">
    <div class="brand">
      <div class="brand-box"></div>
      <div class="brand-name">FERNWAY<br>STRATEGY GROUP</div>
    </div>
    <nav class="nav">
      <a class="active">Home</a><a>Services</a><a>Research</a><a>The Institute</a><a>In the News</a>
    </nav>
    <div class="header-icon" style="left:898px">
      <svg width="22" height="22" viewBox="0 0 22 22"><circle cx="10" cy="10" r="4.5" fill="none" stroke="#fff" stroke-width="1.4"/><path d="M13.3 13.3l3.5 3.5" stroke="#fff" stroke-width="1.4"/></svg>
    </div>
    <div class="header-icon" style="left:929px">
      <svg width="22" height="22" viewBox="0 0 22 22"><circle cx="11" cy="8.5" r="3.2" fill="#fff"/><path d="M5 17c1-3.5 3.4-5 6-5s5 1.5 6 5z" fill="#fff"/></svg>
    </div>
    <div class="btn-outline" style="left:969px;top:22px;width:109px;height:31px">Contact Us</div>
  </header>

  <h1 class="abs hero-title">FERNWAY</h1>
  <p class="abs hero-sub">Macroeconomic &amp; policy Analytics<br>for today’s turbulent environment.</p>
  <div class="play" style="left:130px;top:474px;width:52px;height:52px;box-shadow:0 0 0 6px rgba(255,255,255,.25)">
    <svg width="26" height="26" viewBox="0 0 26 26"><circle cx="13" cy="13" r="12" fill="#111"/><path d="M10 8l8 5-8 5z" fill="#fff"/></svg>
  </div>

  <!-- services -->
  <h2 class="section-title" style="top:590px">Our Services</h2>

  <div class="service" style="left:123px">
    <div class="service-icon"><svg width="36" height="36" viewBox="0 0 36 36" fill="none" stroke="#fff" stroke-width="1.6"><circle cx="15" cy="15" r="10"/><path d="M22 22l9 9"/><path d="M9 18l4-4 3 3 5-6"/></svg></div>
    <div class="service-label">Analytics &amp; Messaging <svg width="20" height="10" viewBox="0 0 20 10"><path d="M0 5h18M14 1l4 4-4 4" stroke="#222" stroke-width="1.4" fill="none"/></svg></div>
    <div class="service-photo" role="img" aria-label="Laptop showing an analytics dashboard on a glossy desk" style="background:linear-gradient(160deg,#6b6f74 0%,#cfd6d8 40%,#2c2f33 75%,#0f1012 100%)"></div>
  </div>
  <div class="service" style="left:447px">
    <div class="service-icon"><svg width="36" height="36" viewBox="0 0 36 36" fill="none" stroke="#fff" stroke-width="1.6"><rect x="9" y="5" width="18" height="26" rx="2"/><circle cx="18" cy="14" r="4"/><path d="M13 22h10M13 26h10"/></svg></div>
    <div class="service-label">Customized Reports <svg width="20" height="10" viewBox="0 0 20 10"><path d="M0 5h18M14 1l4 4-4 4" stroke="#222" stroke-width="1.4" fill="none"/></svg></div>
    <div class="service-photo" role="img" aria-label="Hands turning pages of a printed report" style="background:linear-gradient(150deg,#3f4650 0%,#1f242b 40%,#8b8478 75%,#4b4740 100%)"></div>
  </div>
  <div class="service" style="left:771px">
    <div class="service-icon"><svg width="36" height="36" viewBox="0 0 36 36" fill="none" stroke="#fff" stroke-width="1.6"><rect x="8" y="5" width="20" height="26" rx="2"/><path d="M12 12l2 2 3-4M12 20l2 2 3-4M20 12h5M20 20h5"/></svg></div>
    <div class="service-label">Proprietary Surveys <svg width="20" height="10" viewBox="0 0 20 10"><path d="M0 5h18M14 1l4 4-4 4" stroke="#222" stroke-width="1.4" fill="none"/></svg></div>
    <div class="service-photo" role="img" aria-label="Laptop and tablet on a desk with survey printouts" style="background:linear-gradient(135deg,#d8c79a 0%,#9c9a6e 35%,#e9e4d6 65%,#b8b0a0 100%)"></div>
  </div>

  <div class="btn-outline" style="left:528px;top:1061px;width:144px;height:35px">View All Services</div>

  <!-- about -->
  <section class="abs about">
    <h2 class="abs about-title">About Us</h2>
    <p class="abs about-text">Our services suite focuses on providing exclusive, custom research and analytics to a select number of clients.&nbsp; We do so by outlining a sophisticated research plan, building teams of industry experts, and providing final analyses catered to your preferred audience.</p>
    <div class="btn-outline" style="left:660px;top:91px;width:115px;height:35px">Read More</div>
    <div class="abs about-frame"></div>
    <div class="abs about-photo" role="img" aria-label="Night view of a domed cathedral and a footbridge over a river"></div>
    <div class="play" style="left:370px;top:358px;width:52px;height:52px;box-shadow:0 0 0 6px rgba(255,255,255,.25)">
      <svg width="26" height="26" viewBox="0 0 26 26"><circle cx="13" cy="13" r="12" fill="#111"/><path d="M10 8l8 5-8 5z" fill="#fff"/></svg>
    </div>
    <div class="abs about-vertical">FERNWAY</div>
  </section>

  <!-- partners -->
  <h2 class="section-title" style="top:1777px">Our Partners</h2>
  <div class="carousel-dot" style="left:87px"><svg width="8" height="10" viewBox="0 0 8 10"><path d="M6 1L2 5l4 4" stroke="#333" stroke-width="1.6" fill="none"/></svg></div>
  <div class="partner" style="left:122px">Harbor Ledger</div>
  <div class="partner" style="left:315px">Meridian Wire</div>
  <div class="partner" style="left:508px">Calder Weekly</div>
  <div class="partner" style="left:701px">Northquay Markets</div>
  <div class="partner" style="left:895px">Open Dial Radio</div>
  <div class="carousel-dot" style="left:1093px"><svg width="8" height="10" viewBox="0 0 8 10"><path d="M2 1l4 4-4 4" stroke="#333" stroke-width="1.6" fill="none"/></svg></div>

  <!-- testimonial -->
  <div class="abs testimonial-band" role="img" aria-label="Muted monochrome city skyline behind the testimonial"></div>
  <div class="abs testimonial-ghost">FERNWAY</div>
  <h2 class="abs testimonial-title">What Our Clients Say</h2>
  <div class="abs avatar" role="img" aria-label="Reviewer portrait"></div>
  <div class="abs reviewer">Arlen Voss<small>21 April 2024</small></div>
  <div class="abs stars">
    <svg width="75" height="13" viewBox="0 0 75 13" fill="#f2c511"><path id="st" d="M6.5 0l1.9 4.2 4.6.4-3.5 3 1.1 4.5-4.1-2.4-4.1 2.4 1.1-4.5-3.5-3 4.6-.4z"/><use href="#st" x="15"/><use href="#st" x="30"/><use href="#st" x="45"/><use href="#st" x="60"/></svg>
  </div>
  <svg class="abs" style="left:122px;top:2196px" width="32" height="24" viewBox="0 0 32 24" fill="#8d8d8d"><path d="M0 24V12C0 5 4 1 12 0v5c-4 1-6 3-6 7h6v12zM18 24V12c0-7 4-11 12-12v5c-4 1-6 3-6 7h6v12z"/></svg>
  <p class="abs quote-text">Lorem Ipsum is simply dummy text of the printing and typesetting industry. Lorem Ipsum has been the industry's standard dummy text ever since the 1500s, when an unknown printer took a galley of type and scrambled it to make a type specimen book.</p>
  <div class="abs arrow-pair">
    <span><svg width="22" height="10" viewBox="0 0 22 10"><path d="M22 5H2M6 1L2 5l4 4" stroke="#fff" stroke-width="1.4" fill="none"/></svg></span>
    <span><svg width="22" height="10" viewBox="0 0 22 10"><path d="M0 5h20M16 1l4 4-4 4" stroke="#fff" stroke-width="1.4" fill="none"/></svg></span>
  </div>
  <div class="abs portrait-frame"></div>
  <div class="abs portrait" role="img" aria-label="Client in a dark blazer standing with arms crossed"></div>

  <!-- news -->
  <div class="abs news-feature" role="img" aria-label="Hands working with a glowing digital medical technology interface"></div>
  <div class="abs news-strip">FERNWAY STRATEGY</div>
  <div class="abs" style="left:132px;top:2843px">
    <div class="news-date"><svg width="16" height="16" viewBox="0 0 16 16" fill="none" stroke="#d89b8f" stroke-width="1.2"><rect x="1.5" y="2.5" width="13" height="12"/><path d="M1.5 6h13M5 1v3M11 1v3M4 9h2M7 9h2M10 9h2M4 12h2M7 12h2"/></svg>February 28, 2024</div>
    <p class="news-head" style="margin-top:12px;width:490px">“Medical Technology Industry Continues to Create High-Paying<br>&nbsp;Jobs at Small Businesses Throughout Pandemic.”</p>
    <svg class="news-arrow" style="margin:6px 0 0 6px" width="18" height="10" viewBox="0 0 18 10"><path d="M0 5h16M12 1l4 4-4 4" stroke="#d89b8f" stroke-width="1.3" fill="none"/></svg>
  </div>

  <h2 class="abs latest-title">Latest News</h2>
  <div class="thumb" style="top:2608px;background:linear-gradient(135deg,#e9e7e2 0%,#8a6a3a 40%,#3a2b4a 70%,#d8d4cc 100%)" role="img" aria-label="Spilled medicine capsules"></div>
  <div class="news-item" style="top:2608px">
    <div class="news-date"><svg width="16" height="16" viewBox="0 0 16 16" fill="none" stroke="#d89b8f" stroke-width="1.2"><rect x="1.5" y="2.5" width="13" height="12"/><path d="M1.5 6h13M5 1v3M11 1v3"/></svg>February 28, 2024</div>
    <p class="news-head">Dr. Castell: Careplan’s drug price ‘negotiations’ are anything but</p>
    <svg style="margin-top:4px" width="18" height="10" viewBox="0 0 18 10"><path d="M0 5h16M12 1l4 4-4 4" stroke="#d89b8f" stroke-width="1.3" fill="none"/></svg>
  </div>
  <div class="thumb" style="top:2737px;background:linear-gradient(180deg,#4aa0e0 0%,#8fcaf0 35%,#2f7a9a 60%,#3f8a4a 100%)" role="img" aria-label="Aerial view of a sunny waterfront city"></div>
  <div class="news-item" style="top:2736px">
    <div class="news-date"><svg width="16" height="16" viewBox="0 0 16 16" fill="none" stroke="#d89b8f" stroke-width="1.2"><rect x="1.5" y="2.5" width="13" height="12"/><path d="M1.5 6h13M5 1v3M11 1v3"/></svg>February 28, 2024</div>
    <p class="news-head">“New Data Finds Medtech Industry Thrives in the Sunshine State.”</p>
    <svg style="margin-top:4px" width="18" height="10" viewBox="0 0 18 10"><path d="M0 5h16M12 1l4 4-4 4" stroke="#d89b8f" stroke-width="1.3" fill="none"/></svg>
  </div>
  <div class="btn-outline" style="left:744px;top:2866px;width:122px;height:35px">View All News</div>

  <!-- contact -->
  <div class="abs map" role="img" aria-label="Street map of the office neighbourhood"></div>
  <svg class="abs" style="left:300px;top:3143px" width="22" height="30" viewBox="0 0 22 30"><path d="M11 0C5 0 0 5 0 11c0 8 11 19 11 19s11-11 11-19C22 5 17 0 11 0z" fill="#e0392b"/><circle cx="11" cy="11" r="4" fill="#8a1a12"/></svg>
  <div class="abs map-card">418 Larkspur Ave, Suite<br>210, Halden, NR 40112</div>
  <div class="abs contact-panel"></div>
  <h2 class="abs contact-title">For any Inquiries,<br>Please Call or Email us.</h2>
  <p class="abs contact-sub">Alternatively you can fill in the following contact form.</p>
  <div class="field" style="top:3142px;height:36px">Name</div>
  <div class="field" style="top:3191px;height:36px">Email</div>
  <div class="field" style="top:3239px;height:75px">Message</div>
  <div class="abs submit">SUBMIT</div>

  <!-- footer -->
  <footer class="site-footer">
    <div class="brand">
      <div class="brand-box"></div>
      <div class="brand-name">FERNWAY<span>STRATEGY GROUP</span></div>
    </div>
    <div class="footer-divider" style="left:389px"></div>
    <div class="footer-divider" style="left:638px"></div>
    <div class="footer-divider" style="left:920px"></div>

    <h3 class="footer-heading" style="left:478px">About Us</h3>
    <ul class="footer-links"><li>Home</li><li>Home</li><li>Services</li><li>Research</li><li>The Institute</li><li>In the News</li><li>Contact Us</li></ul>

    <h3 class="footer-heading" style="left:706px">Contact Us</h3>
    <div class="contact-row" style="top:3485px"><span class="ring"><svg width="10" height="12" viewBox="0 0 10 12"><path d="M5 0C2.2 0 0 2.2 0 5c0 3.5 5 7 5 7s5-3.5 5-7C10 2.2 7.8 0 5 0z" fill="#fff"/><circle cx="5" cy="5" r="1.8" fill="#0d0d0d"/></svg></span><span>418 Larkspur Ave Suite 210<br>Halden, NR 40112</span></div>
    <div class="contact-row" style="top:3528px"><span class="ring"><svg width="10" height="8" viewBox="0 0 10 8" fill="none" stroke="#fff" stroke-width="1"><rect x=".5" y=".5" width="9" height="7"/><path d="M.5 .5l4.5 4 4.5-4"/></svg></span><span>info@FernwayStrategy.com</span></div>
    <div class="contact-row" style="top:3567px"><span class="ring"><svg width="10" height="10" viewBox="0 0 10 10"><path d="M2 0l2 2.5-1.2 1.3c.6 1.3 1.6 2.3 2.9 2.9L7 5.5 9.5 7.5 8.5 9.5C4 9.5.5 6 .5 1.5z" fill="#fff"/></svg></span><span>+ (555) 014-2270</span></div>

    <h3 class="footer-heading" style="left:998px">Follow Us</h3>
    <div class="social-row" style="top:3485px"><span class="ring"></span>Friendline</div>
    <div class="social-row" style="top:3525px"><span class="ring"></span>Workgraph</div>
    <div class="social-row" style="top:3565px"><span class="ring"></span>Chirpstream</div>

    <div class="abs footer-rule"></div>
    <p class="abs copyright">© 2024 FERNWAY STRATEGY GROUP ALL RIGHTS RESERVED</p>
  </footer>

</div>
</body>
</html>
```